LOS PINOS DE ARENA - EXCLUSIVE AND LUXURY REAL ESTATE PROJECT

Se trata del diseño de un mono poste grande (4 m x 2 m) o (8m x 3m) anunciando la construcción de 30 villas de lujo en un terreno en primera línea de playa en el sur de España (Cádiz).

La idea es crear expectación y transmitir lujo y exclusividad.

Target Market(s)

Clientes de alto poder adquisitivo que quieran adquirir su segunda vivienda en un entorno privilegiado a escasos pasos de una de las playas más bonitas de Cádiz.

Industry/Entity Type

REAL ESTATE

Colors

Designer to choose colors to be used in the design.

Requirements
Must have
• LOS PINOS DE ARENA as the name of the development
Nice to have
• Crear expectación con ideas del tipo: “Coming soon” o “No te lo puedes perder”

```html
<!DOCTYPE html>
<html lang="es">
<head>
<meta charset="UTF-8">
<title>Los Pinos de Arena — Coming soon</title>
<link rel="stylesheet" href="https://fonts.googleapis.com/css2?family=Jost:wght@300;400&display=swap">
<style>
  :root {
    --ink: #0a0a0a;
    --paper: #ffffff;
    --sea-light: #eef6fb;
    --sea-mid: #b3dcf3;
  }
  * { margin: 0; padding: 0; box-sizing: border-box; }
  html, body {
    width: 1200px;
    height: 720px;
    overflow: hidden;
    background: var(--paper);
  }
  .billboard {
    position: relative;
    width: 1200px;
    height: 720px;
    background: var(--paper);
    font-family: "Jost", "Futura", sans-serif;
    color: var(--ink);
  }
  .billboard__frame {
    position: absolute;
    left: 41px;
    top: 82px;
    width: 1118px;
    height: 561px;
    border: 3.5px solid var(--ink);
    overflow: hidden;
  }
  .billboard__wave {
    position: absolute;
    left: 0;
    bottom: 0;
    width: 100%;
    height: 100%;
  }
  .brand-mark {
    position: absolute;
    left: 0;
    right: 0;
    top: 118px;
    display: flex;
    justify-content: center;
    align-items: center;
    gap: 22px;
  }
  .brand-mark__square {
    width: 54px;
    height: 54px;
    background: var(--sea-mid);
  }
  .brand-mark__name {
    font-weight: 300;
    font-size: 190px;
    line-height: 1;
    letter-spacing: 0.04em;
    color: var(--ink);
  }
  .project-name {
    position: absolute;
    left: 80px;
    right: 80px;
    top: 424px;
    text-align: center;
    font-weight: 300;
    font-size: 54px;
    line-height: 1;
    letter-spacing: 0.28em;
    padding-left: 0.28em;
    white-space: nowrap;
  }
  .teaser {
    position: absolute;
    left: 0;
    right: 0;
    top: 566px;
    text-align: center;
    font-weight: 300;
    font-size: 54px;
    line-height: 1;
    letter-spacing: 0.03em;
  }
</style>
</head>
<body>
  <main class="billboard">
    <div class="billboard__frame">
      <svg class="billboard__wave" viewBox="0 0 1111 554" preserveAspectRatio="none" aria-hidden="true">
        <path d="M0 477 C 120 500, 300 503, 520 490 C 760 476, 960 440, 1111 427 L1111 554 L0 554 Z" fill="var(--sea-light)"/>
      </svg>
    </div>

    <div class="brand-mark">
      <span class="brand-mark__square"></span>
      <span class="brand-mark__name">LPA</span>
    </div>

    <h1 class="project-name">LOS PINOS DE ARENA</h1>
    <p class="teaser">coming soon...</p>
  </main>
</body>
</html>
```